Vacation giveaway landing page design

We are giving away a holiday/vacation to Rome and we need a landing page designed that will entice people to enter their email address for a chance to win!

Full brief, examples and everything else can be found in this document: https://files.brintowle.net/papers/p/4-wxkoppTR7mnbQ2vyLazcR5xsjfPe3lhmwcKt27r/view?mode=linked

1 page

```html
<!DOCTYPE html>
<html lang="en">
<head>
<meta charset="utf-8">
<title>The Wish Weavers – Win a trip to Rome</title>
<link rel="stylesheet" href="https://fonts.googleapis.com/css2?family=Khand:wght@500;600;700&family=Rajdhani:wght@500;600;700&family=Dancing+Script:wght@500&display=swap">
<style>
:root{
  --teal:#35c3bb;
  --teal-bright:#19d3d0;
  --teal-title:#30b9b1;
  --blue-link:#1c7fa6;
  --grey-label:#7a7a7a;
  --red:#d93a33;
  --white:#ffffff;
  --card-text:#3b3b3b;
  --card-border:#e2e2e2;
  --fb-link:#3b5998;
}
*{margin:0;padding:0;box-sizing:border-box}
html,body{width:1074px;height:1200px;overflow:hidden;background:var(--white)}
body{position:relative;font-family:"Rajdhani",sans-serif;color:var(--white)}
.hero{position:absolute;left:0;top:0;width:1074px;height:539px;
  background:linear-gradient(180deg,#2f2f6e 0%,#4b3f7c 28%,#6a4a6a 48%,#7a5232 70%,#3d2a1a 100%)}
.brand{position:absolute;left:67px;top:27px;display:flex;align-items:center;gap:8px}
.brand-dot{width:26px;height:26px;border-radius:50%;background:var(--white)}
.brand-name{font-family:"Khand",sans-serif;font-weight:700;font-size:17px;line-height:15px;letter-spacing:.5px;color:var(--white);text-transform:uppercase}
.headline-box{position:absolute;left:87px;top:120px;width:397px;height:126px;background:rgba(255,255,255,.2)}
.headline-kicker{position:absolute;left:24px;top:22px;font-size:15px;font-weight:600;letter-spacing:3.6px;white-space:nowrap;line-height:18px}
.headline-main{position:absolute;left:23px;top:36px;font-family:"Rajdhani",sans-serif;font-weight:700;font-size:54px;line-height:54px;letter-spacing:1px;color:#e8e6ef;white-space:nowrap}
.headline-main .city{color:var(--teal-bright)}
.headline-script{position:absolute;left:212px;top:91px;font-family:"Dancing Script",cursive;font-size:11.5px;line-height:14px;letter-spacing:.5px;white-space:nowrap}
.offer{position:absolute;left:0;top:355px;width:1074px;text-align:center;font-size:15.5px;font-weight:600;letter-spacing:1.8px;line-height:22px}
.offer strong{display:block;font-size:19px;font-weight:700;letter-spacing:3px;margin-top:2px}
.signup{position:absolute;left:430px;top:447px;display:flex;gap:4px}
.signup-input{width:157px;height:23px;background:var(--white);border-radius:2px;color:#8a8a8a;font-size:8.5px;padding:6px 11px;font-weight:500;letter-spacing:.3px}
.signup-button{width:54px;height:23px;background:var(--red);border-radius:2px;font-family:"Khand",sans-serif;font-weight:700;font-size:10px;letter-spacing:.6px;text-align:center;line-height:23px}
.consent{position:absolute;left:0;top:483px;width:1074px;text-align:center;font-size:5.6px;font-weight:700}
.winners-title{position:absolute;left:0;top:588px;width:1087px;text-align:center;font-family:"Khand",sans-serif;font-weight:700;font-size:22px;color:var(--teal-title);letter-spacing:.3px}
.post{position:absolute;width:140px;background:var(--white);border:1px solid var(--card-border);font-family:Arial,Helvetica,sans-serif;color:var(--card-text)}
.post-photo{position:relative;height:115px}
.post-head{position:absolute;left:4px;top:4px;display:flex;gap:5px}
.post-avatar{width:24px;height:24px;background:var(--white)}
.post-author{font-size:7.6px;font-weight:700;color:var(--white);line-height:9px;padding-top:2px}
.post-author small{display:block;font-weight:400;font-size:6.3px;color:#eee}
.post-badge{position:absolute;right:6px;top:6px;width:9px;height:9px;background:var(--white);border-radius:1px}
.post-body{padding:9px 7px 0;font-size:7.4px;line-height:10.6px;color:var(--card-text)}
.post-body p{margin-bottom:3px;color:var(--card-text)}
.post-body a{color:var(--fb-link);text-decoration:none}
.post-stats{margin:6px 7px 0;border-top:1px solid #eee;padding:6px 0 7px;display:flex;gap:12px;font-size:6.2px;color:#777;font-weight:700}
.post-stats span{display:flex;align-items:center;gap:3px}
.post-stats svg{width:7px;height:7px;fill:#888}
.winner-label{position:absolute;width:200px;text-align:center;font-family:"Khand",sans-serif;font-weight:700;line-height:18px}
.winner-month{font-size:14px;color:var(--grey-label)}
.winner-prize{font-size:12px;color:var(--blue-link)}
.footer{position:absolute;left:0;top:1005px;width:1074px;height:195px;background:var(--teal);font-family:"Khand",sans-serif}
.footer-nav{position:absolute;left:0;top:50px;width:1087px;display:flex;justify-content:center;gap:37px;font-weight:700;font-size:13px;letter-spacing:.2px}
.footer-legal{position:absolute;left:0;top:119px;width:1087px;text-align:center;font-weight:500;font-size:7.4px;line-height:13.5px}
</style>
</head>
<body>

<section class="hero" role="img" aria-label="Photograph of Rome at dusk: a domed basilica lit up above a stone bridge under a purple evening sky">
  <div class="brand"><span class="brand-dot"></span><span class="brand-name">The Wish<br>Weavers</span></div>

  <div class="headline-box">
    <div class="headline-kicker">ENTER FOR YOUR CHANCE TO FLY AWAY</div>
    <div class="headline-main">TO <span class="city">ROME</span></div>
    <div class="headline-script">on an all inclusive vacation</div>
  </div>

  <div class="offer">ENTER FOR A CHANCE TO WIN A<br>ONE-WEEK VACATION FOR TWO AT THE<strong>ROME</strong></div>

  <form class="signup">
    <div class="signup-input">Enter you email</div>
    <div class="signup-button">ENTER</div>
  </form>
  <p class="consent">“By entering your email address, you agree to receive updates about the competition and The Wish Weavers. You can review our competition terms and conditions here.”</p>
</section>

<h2 class="winners-title">PREVIOUS WINNERS</h2>

<article class="post" style="left:187px;top:638px">
  <div class="post-photo" role="img" aria-label="Photo of June's winner outdoors by a canal" style="background:linear-gradient(135deg,#5d6b5a,#3a3430 55%,#9aa89a)">
    <div class="post-head"><span class="post-avatar"></span><div class="post-author">The Wish Weavers<small>about 8 months ago</small></div></div>
    <span class="post-badge"></span>
  </div>
  <div class="post-body">
    <p>This month's winner is just too kind 🙂</p>
    <p>Sam Ortega won a trip to the Canary Islands but has decided to give the prize to his parents who have always wanted to go. Congrats to Sam and his parents!</p>
    <p>Feeling lucky? Click here for your chance to win a trip to Valencia - <a>https://wishwe.link/val</a></p>
  </div>
  <div class="post-stats"><span><svg viewBox="0 0 8 8"><path d="M0 3h2v5H0zM3 3l2-3 1 1-1 2h3v2l-1 3H3z"/></svg>15</span><span><svg viewBox="0 0 8 8"><path d="M0 0h8v5H3L1 7V5H0z"/></svg>3</span><span><svg viewBox="0 0 8 8"><path d="M5 0l3 3-3 3V4C2 4 1 5 0 7c0-3 2-5 5-5z"/></svg>1</span></div>
</article>

<article class="post" style="left:467px;top:646px">
  <div class="post-photo" role="img" aria-label="Photo of July's winner standing in a doorway" style="background:linear-gradient(135deg,#2d2a6a,#6a5a8a 50%,#8a3a2a)">
    <div class="post-head"><span class="post-avatar"></span><div class="post-author">The Wish Weavers<small>about 6 months ago</small></div></div>
    <span class="post-badge"></span>
  </div>
  <div class="post-body">
    <p>Looks like Nina is the lucky one this month as she's won a trip to Valencia! What a Christmas present!</p>
    <p>Want something to look forward to in the New Year? You could win a trip to see the Northern Lights by signing up here - <a>https://wishwe.link/aurora</a></p>
  </div>
  <div class="post-stats"><span><svg viewBox="0 0 8 8"><path d="M0 3h2v5H0zM3 3l2-3 1 1-1 2h3v2l-1 3H3z"/></svg>18</span><span><svg viewBox="0 0 8 8"><path d="M0 0h8v5H3L1 7V5H0z"/></svg>Comment</span><span><svg viewBox="0 0 8 8"><path d="M5 0l3 3-3 3V4C2 4 1 5 0 7c0-3 2-5 5-5z"/></svg>2</span></div>
</article>

<article class="post" style="left:747px;top:639px">
  <div class="post-photo" role="img" aria-label="Photo of August's winner on a green mountain hillside" style="background:linear-gradient(180deg,#8a98a8,#6a7a5a 45%,#4a5a3a)">
    <div class="post-head"><span class="post-avatar"></span><div class="post-author">The Wish Weavers<small>about 9 months ago</small></div></div>
    <span class="post-badge"></span>
  </div>
  <div class="post-body">
    <p>🎉 Our lucky winner of this month's prize draw is... Clara Vinet! 🎉</p>
    <p>A HUGE congratulations to her as she's jetting off to the Algarve in Portugal for an incredible week in the sun!</p>
    <p>Next month's giveaway is a trip to the Canary Islands - find out more here: <a>https://wishwe.link/canary</a></p>
  </div>
  <div class="post-stats"><span><svg viewBox="0 0 8 8"><path d="M0 3h2v5H0zM3 3l2-3 1 1-1 2h3v2l-1 3H3z"/></svg>21</span><span><svg viewBox="0 0 8 8"><path d="M0 0h8v5H3L1 7V5H0z"/></svg>5</span><span><svg viewBox="0 0 8 8"><path d="M5 0l3 3-3 3V4C2 4 1 5 0 7c0-3 2-5 5-5z"/></svg>1</span></div>
</article>

<div class="winner-label" style="left:156px;top:919px"><div class="winner-month">JUNE'S WINNERS</div><div class="winner-prize">A WEEK IN PORTUGAL</div></div>
<div class="winner-label" style="left:436px;top:919px"><div class="winner-month">JULY'S WINNERS</div><div class="winner-prize">A WEEK IN PORTUGAL</div></div>
<div class="winner-label" style="left:717px;top:919px"><div class="winner-month">AUGUST'S WINNERS</div><div class="winner-prize">A WEEK IN PORTUGAL</div></div>

<footer class="footer">
  <nav class="footer-nav"><span>CONTACT US</span><span>TERMS &amp; CONDITIONS</span><span>PRIVACY POLICY</span></nav>
  <p class="footer-legal">Contact: +44 (0) 20 7946 0182 | Email: hello@wishweavers.example<br>© 2017 Brightmere Quill LTD a private limited company registered in England and Wales, Reg No: 12345670. Reg office and postal address: 14 Harbour Row, London, SE1 0AA, UK</p>
</footer>

</body>
</html>
```